Amber Lantern Cafe Business Card

We need a business card design for a new European Cafe. Main menu will be coffee and deserts.

Requirements
Must have
• Logo - 1 of the attached versions
Address - TBA (you can use 487 Morrow Ave Unit 9 for now)
Phone - TBA (you can use 555-238-4176 for now)

```html
<!DOCTYPE html>
<html lang="en">
<head>
<meta charset="utf-8">
<title>Amber Lantern Cafe – Business Card</title>
<link rel="stylesheet" href="https://fonts.googleapis.com/css2?family=Open+Sans:wght@600&display=swap">
<style>
  :root {
    --backdrop: #6a6a6a;
    --card-red: #b41f27;
    --card-red-mid: #8f161c;
    --card-red-deep: #4a080b;
    --ink-white: #ffffff;
  }
  html, body {
    margin: 0;
    padding: 0;
    width: 1200px;
    height: 900px;
    overflow: hidden;
    background: var(--backdrop);
  }
  .canvas {
    position: relative;
    width: 1200px;
    height: 900px;
  }
  .business-card {
    position: absolute;
    left: 76px;
    top: 130px;
    width: 1060px;
    height: 612px;
    border-radius: 22px;
    overflow: hidden;
    background:
      radial-gradient(ellipse 62% 70% at 58% 48%, var(--card-red) 0%, var(--card-red) 45%, var(--card-red-mid) 78%, var(--card-red-deep) 100%);
  }
  .background-motif {
    position: absolute;
    left: 0;
    top: 0;
    width: 480px;
    height: 612px;
  }
  .brand-lockup {
    position: absolute;
    left: 0;
    right: 0;
    top: 147px;
    display: flex;
    flex-direction: column;
    align-items: center;
    font-family: "Open Sans", sans-serif;
    font-weight: 600;
    color: var(--ink-white);
  }
  .brand-square {
    width: 174px;
    height: 174px;
    border-radius: 6px;
    background: var(--ink-white);
    margin-left: 10px;
  }
  .brand-name {
    margin: 0;
    font: inherit;
    text-align: center;
    line-height: 1;
  }
  .brand-name-main {
    display: block;
    margin-top: 34px;
    font-size: 54px;
    letter-spacing: 0.3px;
  }
  .brand-name-sub {
    display: block;
    margin-top: 12px;
    font-size: 40px;
    letter-spacing: 1px;
  }
  .card-contact {
    position: absolute;
    left: 0;
    right: 0;
    bottom: 42px;
    margin: 0;
    text-align: center;
    font-family: "Open Sans", sans-serif;
    font-weight: 600;
    font-size: 20px;
    line-height: 1.5;
    color: var(--ink-white);
    font-style: normal;
    letter-spacing: 0.5px;
  }
  .contact-divider {
    margin: 0 14px;
  }
</style>
</head>
<body>
  <main class="canvas">
    <section class="business-card" aria-label="Amber Lantern Cafe business card front">
      <svg class="background-motif" viewBox="0 0 480 612" role="img" aria-label="Faint decorative swirl motif in the card background">
        <defs>
          <radialGradient id="motifShade" cx="0.35" cy="0.55" r="0.6">
            <stop offset="0" stop-color="#5a0a0e" stop-opacity="0.35"/>
            <stop offset="1" stop-color="#5a0a0e" stop-opacity="0"/>
          </radialGradient>
        </defs>
        <rect width="480" height="612" fill="url(#motifShade)"/>
      </svg>
      <div class="brand-lockup">
        <div class="brand-square" aria-hidden="true"></div>
        <h1 class="brand-name">
          <span class="brand-name-main">Amber Lantern</span>
          <span class="brand-name-sub">Cafe</span>
        </h1>
      </div>
      <address class="card-contact">
        487 Morrow Ave Unit 9<span class="contact-divider">|</span>555-238-4176
      </address>
    </section>
  </main>
</body>
</html>
```